Brightmeadow Charity Ball Poster

We are looking for a poster for our upcoming event, "Brightmeadow Charity Ball" - a sit down dinner formal event hosted by our university club, OKRU.
Usually we source designs internally from our committee (even if they aren't the most amazing quality), however this time round we have no one available to do it as everyone is a volunteer.
The event's theme is 'winter wonderland', based around the snowy forests you see in Velmoria or Crown of Ashes (neither of these specific things are the theme however). Our venue is a clear-roof marque in a space surrounded by very tall pine trees giving off the forest vibe, and there are festoons strung between the trees so this is an element of warm light amongst the forest, perhaps a building or village tucked away in the forest.
The poster is for printing out at A3 size, and we will also need to create a Chatterbook event cover photo and other marketing graphics from the original poster files so some flexibility in the design and original files are required.
Things that need to be included on the poster :
---Event details
Brightmeadow Charity Ball
Saturday 12th August
7pm – midnight
Harrowgate Auditorium, KPT
Tables of 10
Members - $140
Non members - $150
All profits donated to Stride for Hope
---- Extra info and images (can be at the bottom, in corners etc,)
18+ ID required | Drink Responsibly
OKRU Logo
KPT Guild Logo
(these logos may be changed to black and white if need be)
Example images of styles, colours and the sort of landscape we want for the poster can be found in the document attached.

```html
<!DOCTYPE html>
<html lang="en">
<head>
<meta charset="utf-8">
<title>Brightmeadow Charity Ball</title>
<link rel="stylesheet" href="https://fonts.googleapis.com/css2?family=Chewy&family=Kurale&display=swap">
<style>
  :root {
    --frost-light: #eef7f8;
    --frost-mid: #bfe0e2;
    --frost-deep: #7fb8bd;
    --branch-grey: #8fa6ad;
    --title-top: #fff27a;
    --title-bottom: #f58a2c;
    --title-shade: #2a5a78;
    --details-blue: #2b9ccf;
    --tables-purple: #6a2fa8;
    --price-purple: #7a34c8;
    --profits-magenta: #b42cb4;
    --note-ink: #2f2f35;
    --guild-blue: #1d3fc0;
    --okru-plum: #7a1f5a;
  }
  * { margin: 0; padding: 0; box-sizing: border-box; }
  html, body { width: 849px; height: 1200px; overflow: hidden; background: var(--frost-light); }
  .poster {
    position: relative;
    width: 849px;
    height: 1200px;
    overflow: hidden;
    font-family: "Kurale", serif;
  }
  .forest-scene {
    position: absolute;
    inset: 0;
    background:
      radial-gradient(ellipse at 50% 95%, #f4fbfb 0%, rgba(244,251,251,0) 45%),
      radial-gradient(ellipse at 10% 40%, var(--frost-deep) 0%, rgba(127,184,189,0) 45%),
      radial-gradient(ellipse at 92% 55%, var(--frost-deep) 0%, rgba(127,184,189,0) 45%),
      linear-gradient(180deg, #d7e9ec 0%, var(--frost-mid) 45%, #a9d3d4 70%, #e6f2f3 100%);
  }
  .glow-orb {
    position: absolute;
    left: 112px;
    top: 344px;
    width: 624px;
    height: 624px;
    border-radius: 50%;
    background: radial-gradient(circle, #ffffff 0%, #ffffff 55%, rgba(255,255,255,0.85) 75%, rgba(255,255,255,0) 100%);
  }
  .title {
    position: absolute;
    left: 0;
    width: 100%;
    text-align: center;
    font-family: "Chewy", cursive;
    line-height: 1;
    background: linear-gradient(180deg, var(--title-top) 0%, #ffc94a 50%, var(--title-bottom) 100%);
    -webkit-background-clip: text;
    background-clip: text;
    color: transparent;
    filter: drop-shadow(2px 4px 2px var(--title-shade));
  }
  .title-line-1 { top: 150px; font-size: 84px; transform: rotate(4deg); letter-spacing: 1px; }
  .title-line-2 { top: 238px; font-size: 84px; transform: rotate(5deg); }
  .detail {
    position: absolute;
    left: 0;
    width: 100%;
    text-align: center;
    line-height: 1;
  }
  .event-date { top: 432px; font-size: 38px; color: var(--details-blue); transform: rotate(4deg); }
  .event-time { top: 484px; font-size: 38px; color: var(--details-blue); transform: rotate(2deg); }
  .event-venue { top: 532px; font-size: 34px; color: var(--details-blue); transform: rotate(-4deg); }
  .tables-heading {
    top: 595px; font-size: 38px; color: var(--tables-purple);
  }
  .tables-heading span { border-bottom: 1.5px solid var(--tables-purple); padding: 0 8px 2px; }
  .price { font-size: 36px; color: var(--price-purple); }
  .price-members { top: 645px; }
  .price-non-members { top: 693px; }
  .charity { font-size: 31px; color: var(--profits-magenta); letter-spacing: 0.5px; }
  .charity-line-1 { top: 760px; transform: rotate(2deg); }
  .charity-line-2 { top: 800px; transform: rotate(1deg); }
  .note { font-size: 27px; color: var(--note-ink); }
  .note-age { top: 866px; }
  .note-drink { top: 904px; transform: rotate(3deg); }
  .partner {
    position: absolute;
    top: 1062px;
    display: flex;
    align-items: center;
    gap: 10px;
    font-size: 28px;
    line-height: 1;
  }
  .partner-guild { left: 205px; color: var(--guild-blue); }
  .partner-guild .mark { width: 22px; height: 22px; background: var(--guild-blue); }
  .partner-okru { left: 520px; color: var(--okru-plum); }
  .partner-okru .mark { width: 22px; height: 22px; border-radius: 50%; background: var(--okru-plum); }
</style>
</head>
<body>
  <main class="poster">
    <div class="forest-scene" role="img" aria-label="Frost-covered winter forest with bare snowy trees lining a white path"></div>
    <div class="glow-orb"></div>

    <h1>
      <span class="title title-line-1">BRIGHTMEADOW</span>
      <span class="title title-line-2">CHARITY BALL</span>
    </h1>

    <p class="detail event-date">Saturday, 12th August</p>
    <p class="detail event-time">7pm – midnight</p>
    <p class="detail event-venue">Harrowgate Auditorium, KPT</p>

    <p class="detail tables-heading"><span>Tables of 10</span></p>
    <p class="detail price price-members">Members - $140</p>
    <p class="detail price price-non-members">Non members - $150</p>

    <p class="detail charity charity-line-1">ALL PROFITS DONATED TO</p>
    <p class="detail charity charity-line-2">STRIDE FOR HOPE</p>

    <p class="detail note note-age">18+ ID required</p>
    <p class="detail note note-drink">Drink Responsibly</p>

    <div class="partner partner-guild"><span class="mark"></span>KPT Guild</div>
    <div class="partner partner-okru"><span class="mark"></span>OKRU</div>
  </main>
</body>
</html>
```